PPE EQIUPMENT

WE WOULD LIKE TO PRODUCE 2 DIFFERENT BANNERS TO BE PLACED OUTSIDE OF OUR WAREHOUSE TO ADVERTISE THAT WE HAVE FACE MASKS, HAND SANITISERS, DISINFECTANT SPRAY, FACE SHIELDS AND HAND SOAP. THE SIZE OF EACH BANNER WILL BE , portrait to be (W) 140 cm x (H) 250 cm, with 4 x eyelets. THE BANNER IS TO STATE PPE EQUIPMENT AVAILABLE HERE AND SHOW OUR PHONE NUMBER 0207-946-0318. FINALLY WE WILL REQUIRE SOME IMAGES OF THE PRODUCTS IF YOU CAN SUPPLY THESE. THANKS

```html
<!DOCTYPE html>
<html lang="en">
<head>
<meta charset="utf-8">
<title>PPE Equipment Available</title>
<link rel="stylesheet" href="https://fonts.googleapis.com/css2?family=Bebas+Neue&family=League+Spartan:wght@700&family=Poppins:wght@300;600;700&display=swap">
<style>
  :root {
    --navy: #1f3a70;
    --ink-band: #0e1630;
    --orange: #f7941d;
    --yellow: #ffcc00;
    --white: #ffffff;
    --black: #111111;
    --product-a: #5b6fb8;
    --product-b: #9fd3ea;
  }
  html, body {
    margin: 0;
    padding: 0;
    overflow: hidden;
  }
  .banner {
    position: relative;
    width: 672px;
    height: 1200px;
    overflow: hidden;
    background: var(--navy);
    font-family: "League Spartan", Arial, sans-serif;
  }
  .headline {
    position: absolute;
    top: 108px;
    left: 0;
    width: 672px;
    text-align: center;
    font-family: "Bebas Neue", Impact, sans-serif;
    color: var(--white);
    line-height: 1;
    margin: 0;
  }
  .headline__top {
    display: block;
    font-size: 97px;
    letter-spacing: 0.5px;
  }
  .headline__bottom {
    display: block;
    font-size: 143px;
    margin-top: -6px;
  }
  .products {
    position: absolute;
    top: 345px;
    left: 0;
    width: 672px;
    height: 316px;
    background: var(--ink-band);
  }
  .products__rule {
    position: absolute;
    left: 119px;
    width: 435px;
    height: 3px;
    background: var(--white);
    border-radius: 2px;
  }
  .products__rule--top { top: 15px; }
  .products__rule--bottom { top: 292px; }
  .products__art {
    position: absolute;
    top: 34px;
    left: 60px;
    width: 560px;
    height: 244px;
    border-radius: 12px;
    background: linear-gradient(135deg, var(--product-b) 0%, var(--product-a) 100%);
    opacity: 0.55;
  }
  .stock-list {
    position: absolute;
    top: 715px;
    left: 78px;
    width: 539px;
    margin: 0;
    padding: 0;
    list-style: none;
  }
  .stock-list__item {
    position: relative;
    height: 44px;
    margin-bottom: 6px;
    background: var(--white);
    border-radius: 22px;
    display: flex;
    align-items: center;
  }
  .stock-list__icon {
    width: 37px;
    height: 37px;
    margin-left: 5px;
    flex: none;
  }
  .stock-list__label {
    margin-left: 8px;
    padding-top: 6px;
    font-size: 40px;
    font-weight: 700;
    letter-spacing: 2px;
    color: var(--black);
    white-space: nowrap;
  }
  .footer {
    position: absolute;
    top: 1057px;
    left: 0;
    width: 672px;
    height: 143px;
    background: var(--orange);
  }
  .campaign {
    position: absolute;
    top: 44px;
    left: 67px;
    font-family: "Poppins", Arial, sans-serif;
    line-height: 1;
  }
  .campaign__lead {
    display: block;
    font-size: 11px;
    font-weight: 300;
    color: #2a1a08;
  }
  .campaign__name {
    display: block;
    font-size: 33px;
    font-weight: 700;
    color: var(--white);
    margin-top: 3px;
  }
  .campaign__sub {
    display: block;
    font-size: 11px;
    font-weight: 600;
    color: #2a1a08;
    margin-top: 3px;
  }
  .footer__divider {
    position: absolute;
    top: 40px;
    left: 251px;
    width: 1px;
    height: 58px;
    background: var(--white);
  }
  .footer__phone {
    position: absolute;
    top: 46px;
    left: 270px;
    font-family: "Poppins", Arial, sans-serif;
    font-size: 47px;
    font-weight: 600;
    letter-spacing: 1px;
    line-height: 1;
    color: var(--white);
  }
</style>
</head>
<body>
<main class="banner">
  <h1 class="headline">
    <span class="headline__top">PPE EQUIPMENT</span>
    <span class="headline__bottom">AVAILABLE</span>
  </h1>

  <section class="products">
    <div class="products__rule products__rule--top"></div>
    <div class="products__art" role="img" aria-label="Product illustrations: face shield, infrared thermometer, soap bar, sanitiser pump bottle, digital thermometer, shoe covers, gloves, surgical mask, safety goggles and latex gloves"></div>
    <div class="products__rule products__rule--bottom"></div>
  </section>

  <ul class="stock-list">
    <li class="stock-list__item">
      <svg class="stock-list__icon" viewBox="0 0 40 40" aria-hidden="true"><circle cx="20" cy="20" r="20" fill="var(--yellow)"/><path d="M13 11 L19 20 L13 29 M21 11 L27 20 L21 29" fill="none" stroke="var(--white)" stroke-width="3.5" stroke-linecap="round" stroke-linejoin="round"/></svg>
      <span class="stock-list__label">FACE MASKS</span>
    </li>
    <li class="stock-list__item">
      <svg class="stock-list__icon" viewBox="0 0 40 40" aria-hidden="true"><circle cx="20" cy="20" r="20" fill="var(--yellow)"/><path d="M13 11 L19 20 L13 29 M21 11 L27 20 L21 29" fill="none" stroke="var(--white)" stroke-width="3.5" stroke-linecap="round" stroke-linejoin="round"/></svg>
      <span class="stock-list__label">HAND SANITISERS</span>
    </li>
    <li class="stock-list__item">
      <svg class="stock-list__icon" viewBox="0 0 40 40" aria-hidden="true"><circle cx="20" cy="20" r="20" fill="var(--yellow)"/><path d="M13 11 L19 20 L13 29 M21 11 L27 20 L21 29" fill="none" stroke="var(--white)" stroke-width="3.5" stroke-linecap="round" stroke-linejoin="round"/></svg>
      <span class="stock-list__label">DISINFECTANT SPRAY</span>
    </li>
    <li class="stock-list__item">
      <svg class="stock-list__icon" viewBox="0 0 40 40" aria-hidden="true"><circle cx="20" cy="20" r="20" fill="var(--yellow)"/><path d="M13 11 L19 20 L13 29 M21 11 L27 20 L21 29" fill="none" stroke="var(--white)" stroke-width="3.5" stroke-linecap="round" stroke-linejoin="round"/></svg>
      <span class="stock-list__label">FACE SHIELDS</span>
    </li>
    <li class="stock-list__item">
      <svg class="stock-list__icon" viewBox="0 0 40 40" aria-hidden="true"><circle cx="20" cy="20" r="20" fill="var(--yellow)"/><path d="M13 11 L19 20 L13 29 M21 11 L27 20 L21 29" fill="none" stroke="var(--white)" stroke-width="3.5" stroke-linecap="round" stroke-linejoin="round"/></svg>
      <span class="stock-list__label">HAND SOAP</span>
    </li>
    <li class="stock-list__item">
      <svg class="stock-list__icon" viewBox="0 0 40 40" aria-hidden="true"><circle cx="20" cy="20" r="20" fill="var(--yellow)"/><path d="M13 11 L19 20 L13 29 M21 11 L27 20 L21 29" fill="none" stroke="var(--white)" stroke-width="3.5" stroke-linecap="round" stroke-linejoin="round"/></svg>
      <span class="stock-list__label">AND MORE...</span>
    </li>
  </ul>

  <footer class="footer">
    <div class="campaign">
      <span class="campaign__lead">PROTECT YOURSELF FROM</span>
      <span class="campaign__name">COVID-19</span>
      <span class="campaign__sub">CORONAVIRUS</span>
    </div>
    <div class="footer__divider"></div>
    <div class="footer__phone">0207-946-0318</div>
  </footer>
</main>
</body>
</html>
```